Orient Wager Digest Quarterly Magazine

We need a magazine design for a new company based in Asia called Orient Wager Digest (OWD).

OWD provide up to date market information for worldwide executives on relevant gaming issues in Asia, covering:
- specific market and legal challenges
- new regulations and their implications for the
industry
- company operations in different jurisdictions (country specific)
- governance and compliance issues
- financing, HR and technology trends

This magazine design must be high-end and relate more to a business periodical/journal that exhibits reliability and industry expertise than a fashion magazine. For reference purpose see Verdant Magazine and their previous issue. It is important that this design project has synergy with our previous two magazines (see file uploads).

You can also visit http://www.orientwagerdigest-example.com, however we are in the process of updating this website.

Initially, we would like to see a conceptual SCAMP for 3 spread layouts, including the following pages:

- Main country page template full-spread (text, image, snippet and data/diagram/graph)
- Editorial page
- Contents page
- Sponsors page
- Front Cover

Specific Requirements:
Page Width = 200mm
Page Height = 265mm
Trim measurement = we usually use 5mm
Corporate Colors = Red #990000, Green #226727
Gutter measurement for a 60 page mag, give or take
(*note that most of the odd pages will be Advertising pages consisting of a full page image, therefore they will not need much work.)
Images can bleed off page

Must Haves:
experience in magazine design
able to work with google drive
able to plot graphs, design diagrams, charts etc...

To All,

Logo version has just been uploaded.

Cheers

```html
<!DOCTYPE html>
<html lang="en">
<head>
<meta charset="utf-8">
<title>Orient Wager Digest – Macau spread</title>
<link rel="stylesheet" href="https://fonts.googleapis.com/css2?family=Roboto+Slab:wght@100;300;400;700&family=Lora:ital,wght@1,400;1,600&family=Open+Sans:wght@600;700&display=swap">
<style>
  :root {
    --red: #990000;
    --red-bright: #a8161b;
    --green: #226727;
    --green-mid: #4f8a3f;
    --green-pale: #c9dcb7;
    --green-soft: #e3eed9;
    --ink: #3a3a3a;
    --ink-soft: #6c6c6c;
    --paper: #ffffff;
    --backdrop: #e8e8e8;
  }
  * { box-sizing: border-box; margin: 0; padding: 0; }
  html, body { width: 1200px; height: 800px; overflow: hidden; }
  body { background: var(--backdrop); font-family: "Roboto Slab", Georgia, serif; color: var(--ink); }

  .spread { position: absolute; left: 40px; top: 29px; width: 1120px; height: 742px; display: flex; }
  .page { position: relative; width: 560px; height: 742px; background: var(--paper); overflow: hidden; }
  .page--left { border-right: 1px solid #dcdcdc; }

  .folio { position: absolute; top: 10px; font-size: 8px; color: var(--ink-soft); }
  .page--left .folio { left: 18px; }
  .page--right .folio { right: 22px; top: 76px; }

  .hero-photo { position: absolute; left: 0; top: 24px; width: 482px; height: 362px;
    background: linear-gradient(170deg, #c7a4a9 0%, #e2c0a0 22%, #9d8c74 45%, #6f7a5e 62%, #8c6a55 80%, #5d6a5a 100%); }
  .country-title { position: absolute; left: 26px; top: 236px; font-family: "Roboto Slab", serif; font-weight: 100;
    font-size: 82px; letter-spacing: 2px; color: #fff; line-height: 1; }

  .headline-banner { position: absolute; left: 0; top: 306px; width: 508px; height: 74px; }
  .headline-banner svg { position: absolute; inset: 0; }
  .headline { position: absolute; left: 24px; top: 10px; font-family: "Lora", serif; font-style: italic; font-weight: 600;
    font-size: 22px; line-height: 26px; color: #fff; }

  .byline { position: absolute; left: 100px; top: 392px; font-size: 6.5px; color: var(--ink-soft); }
  .standfirst { position: absolute; left: 88px; top: 420px; width: 150px; font-family: "Lora", serif; font-style: italic;
    font-size: 11px; line-height: 14.5px; color: var(--green); }

  .col { position: absolute; font-size: 7.2px; line-height: 10.4px; font-weight: 300; text-align: justify; hyphens: auto; overflow: hidden; }
  .col p + p { margin-top: 6px; }
  .drop { float: left; font-size: 28px; line-height: 22px; padding-right: 3px; color: var(--red); font-weight: 300; }
  .operator { font-family: "Open Sans", sans-serif; font-weight: 700; color: var(--red); }
  .operator::before { content: "• "; }

  .footer { position: absolute; bottom: 36px; font-size: 6.5px; color: var(--ink-soft); letter-spacing: 0.3px; }
  .page--left .footer { left: 30px; }
  .page--right .footer { right: 30px; }

  .section-tab { position: absolute; left: 0; top: 70px; width: 132px; height: 17px; background: var(--green);
    color: #fff; font-size: 7.5px; letter-spacing: 1px; line-height: 17px; padding-left: 24px; }

  .sidebar { position: absolute; left: 356px; top: 186px; width: 176px; }
  .stats { background: var(--green-pale); padding: 6px 6px 6px 6px; height: 108px; position: relative; }
  .stats-title { position: absolute; right: 6px; top: 4px; font-size: 11px; font-weight: 700; color: var(--green); letter-spacing: 0.5px; }
  .stat-row { display: flex; align-items: center; height: 22px; margin-top: 2px; }
  .stat-row:first-of-type { margin-top: 14px; }
  .stat-label { width: 82px; height: 22px; background: var(--green); color: #fff; font-size: 6.5px; line-height: 9px; padding: 2px 4px; }
  .stat-label b { display: block; font-size: 8px; font-weight: 400; }
  .stat-arrow { width: 20px; height: 22px; background: #fff; margin-left: 4px; display: flex; align-items: center; justify-content: center; }
  .stat-change { flex: 1; height: 22px; background: var(--red); color: #fff; font-size: 7px; line-height: 22px; text-align: center; margin-left: 2px; }

  .chart-label { margin-top: 8px; font-size: 7.5px; color: var(--ink); padding-bottom: 3px; border-bottom: 1px solid #ccc; }
  .bar-chart { display: block; margin-top: 4px; }
  .share { display: flex; margin-top: 8px; }
  .legend { list-style: none; width: 80px; font-size: 6px; line-height: 10px; }
  .legend li { display: flex; align-items: center; gap: 4px; }
  .legend i { width: 6px; height: 6px; display: inline-block; }
  .legend span { width: 30px; }

  .key-points { margin-top: 10px; background: var(--red-bright); color: #fff; padding: 9px 10px 12px 12px; list-style: none;
    font-family: "Open Sans", sans-serif; font-weight: 600; font-size: 7.2px; line-height: 10px; }
  .key-points li::before { content: "• "; }
  .key-points li + li { margin-top: 6px; }
</style>
</head>
<body>
<main class="spread">

  <section class="page page--left">
    <span class="folio">08</span>
    <div class="hero-photo" role="img" aria-label="Aerial photograph of Macau skyline and waterfront at dusk"></div>
    <h1 class="country-title">MACAU</h1>
    <div class="headline-banner">
      <svg width="508" height="74" viewBox="0 0 508 74">
        <polygon points="0,6 440,0 456,16 480,60 462,62 0,70" fill="var(--red-bright)"/>
        <polygon points="456,16 508,62 480,60" fill="var(--red)"/>
        <polygon points="0,70 14,70 0,78" fill="#6e0000"/>
      </svg>
      <h2 class="headline">Prospects still seen as bright<br>despite regional competition</h2>
    </div>
    <p class="byline">Text by Staff Writer &nbsp;Photo By Staff Photographer</p>

    <p class="standfirst">Macau turned in a record-breaking performance in 2013, with gross gaming revenue hitting $45 billion and despite increasing competition from regional neighbours, the market is tipped for further growth.</p>

    <div class="col" style="left:254px; top:420px; width:140px; height:280px;">
      <p><span class="drop">I</span>n little more than a decade, the Chinese territory has risen from a sleepy outpost with $2 billion turnover to become a market seven times the size of Las Vegas. Although most analysts don't expect Macau to top last year's 18.6 percent growth rate in 2014, the consensus remains for a solid increase in the low to mid-teens this year. Harbourline Securities recently said the market has the potential to double to $85 billion by 2018. There are several driving factors behind the optimism, including the changing face of the tourist industry in the city. Most industry observers agree the VIP market may have peaked, but the premium mass market is expected to fuel gains - good news for the operators given their bigger margins in the latter. Revenue from mass-market baccarat was</p>
    </div>
    <div class="col" style="left:404px; top:420px; width:136px; height:280px;">
      <p>41.8 percent higher in the third quarter than a year before at $3 billion, the Gaming Inspection and Coordination Bureau says. It made up 26.7 percent of the third-quarter casino gross gaming revenue, the most since the fourth quarter of 2005. Despite this growth, the market is still seen as being relatively untapped. There has also been a huge increase in mass-gaming minimum bets, which have risen from HK$300 two years ago to HK$1,000 now. This is a supply and demand adjustment given the table cap policy. Over the next few years, some 20,000 new hotel rooms are expected to become available and may help further attract the mass market gambler by bringing down the average room rate of Macau's hotels. Casino operators are also likely to benefit</p>
    </div>
    <p class="footer">Orient Wager Digest | March 2014</p>
  </section>

  <section class="page page--right">
    <div class="section-tab">GREATER CHINA</div>
    <span class="folio">09</span>

    <div class="col" style="left:30px; top:96px; width:150px; height:600px;">
      <p>from broadening their appeal to offer more non-gaming attractions, such as shows and other entertainment. The development of the Oceanfield theme park on neighbouring Hengqin island is expected to help this trend and provide much needed overspill for Macau's limited land space.</p>
      <p>Another major driver for Macau will be the growing outbound Chinese travel market. Visitors from the mainland accounted for 63 percent of total arrivals last year. However, only 1 percent of China's more than 1.3 billion people visit Macau, compared with 10 percent of the U.S. population travelling to Las Vegas. Macau's gaming stocks were up about 73 percent in 2013.</p>
      <p><span class="operator">Pearl River Holdings (812:HK)</span> holds the biggest market share with 20 casinos, though that percentage dropped to 23.5 percent in Jan. 2014 from 24.7 percent in 2013. Its $3.2 billion Palazzo Aurelia development is scheduled to come online in 2017. The company has indicated it may be interested in opportunities in Japan. Pearl River's Q3 gaming revenue grew 11.4 percent to HK$21.05 billion while adjusted EBITDA was up 8 percent to HK$2.04 billion.</p>
      <p><span class="operator">Nova Leisure Group (207:HK)</span> grew its market share to 21 percent in Jan. 2014 from 18.6 percent in 2013 with six casinos. The company is investing $2.5 billion in the second phase of its Nova Macau development, which is scheduled to come online in 2015. The expansion will nearly double the capacity of the resort. NLG's Q3 revenue rose 16 percent to HK$16.3 billion while adjusted EBITDA increased 24 percent to HK$3.2 billion ($413 million).</p>
      <p><span class="operator">Lotus Bay Resorts (1182:HK)</span> currently has one casino and a market share of 8.9 percent in Jan. 2014, compared with 11 percent in 2013. Its $4 billion Lotus Bay Palace development is scheduled to come online in the first half of 2016, with approximately 2,000 rooms and</p>
    </div>

    <div class="col" style="left:192px; top:40px; width:152px; height:660px;">
      <p>500 table games. Lotus Bay Q3 net profits increased 18 percent to $240.6 million. Casino revenue as a whole rose by 10.1 percent to $944 million.</p>
      <p><span class="operator">Dune Harbour China (1982:HK)</span> had 21.7 percent market share in Jan. 2014 with four casinos, the same as its 2013 share. Analysts say the company has had a lower room occupancy than rivals in Cotai, meaning it has more potential for revenue growth if it fills the rooms. The company's new developments include the $3 billion The Montclair that is scheduled to come online in 2015. Dune Harbour Q3 revenue rose 43 percent to $2.34 billion. Adjusted EBITDA jumped 61 percent to $786.3 million.</p>
      <p><span class="operator">Jadecrest Entertainment (6818:HK)</span> has three casinos and a market share of 13.7 percent in Jan. 2014, comparable with its 2013 share of 14 percent. Its third quarter revenue rose 24 percent to US$1.25 billion. Jadecrest recently awarded Halvard Construction a $488 million contract to build a six-star hotel. The 39-floor building will be part of the Dreamgate complex and will have 783 bedrooms, a casino, restaurants, conference room and a sky pool. The company is also investing $2.9 billion in its Reel City project, scheduled for mid 2015. Jadecrest will be the first of Macau's operators to expand regionally with the opening of Dreamgate Manila in 2014. It has also expressed interest in expanding in Japan.</p>
      <p><span class="operator">Goldleaf Macau (2262:HK)</span> has one casino and a market share of 11.2 percent in Jan. 2014, growing from 10 percent in 2013. Its new developments include the Goldleaf Cotai, which is a $2.5 billion project scheduled for completion mid 2016. Goldleaf China Q3 revenue rose 22 percent to $808 million. Adjusted earnings before interest, tax, depreciation and amortization were up 25 percent at $191 million. EBITDA lagged the average estimate of $202 million.</p>
    </div>

    <aside class="sidebar">
      <div class="stats">
        <span class="stats-title">STATS</span>
        <div class="stat-row"><div class="stat-label">Y2013 GGR<b>$45b</b></div><div class="stat-arrow"><svg width="12" height="8" viewBox="0 0 12 8"><polyline points="0,7 4,3 7,5 12,0" fill="none" stroke="var(--green)" stroke-width="1.2"/></svg></div><div class="stat-change">+18,6%</div></div>
        <div class="stat-row"><div class="stat-label">DEC 2013<b>$4.19b</b></div><div class="stat-arrow"><svg width="12" height="8" viewBox="0 0 12 8"><polyline points="0,7 4,3 7,5 12,0" fill="none" stroke="var(--green)" stroke-width="1.2"/></svg></div><div class="stat-change">+00,0%</div></div>
        <div class="stat-row"><div class="stat-label">Y2014*<b>$00.0b</b></div><div class="stat-arrow"><svg width="12" height="8" viewBox="0 0 12 8"><polyline points="0,7 4,3 7,5 12,0" fill="none" stroke="var(--green)" stroke-width="1.2"/></svg></div><div class="stat-change">+15,0%</div></div>
        <div class="stat-row"><div class="stat-label">Y2018*<b>$85b</b></div><div class="stat-arrow"><svg width="12" height="8" viewBox="0 0 12 8"><polyline points="0,7 4,3 7,5 12,0" fill="none" stroke="var(--green)" stroke-width="1.2"/></svg></div><div class="stat-change">+00,0%</div></div>
      </div>

      <p class="chart-label">Gross Gaming Revenue</p>
      <svg class="bar-chart" width="176" height="110" viewBox="0 0 176 110" font-family="Roboto Slab, serif" font-size="6" fill="#555">
        <text x="140" y="8">In billion US$</text>
        <g stroke="#e2e2e2" stroke-width="0.6">
          <line x1="14" y1="20" x2="172" y2="20"/><line x1="14" y1="38" x2="172" y2="38"/>
          <line x1="14" y1="56" x2="172" y2="56"/><line x1="14" y1="74" x2="172" y2="74"/>
        </g>
        <text x="4" y="22">8</text><text x="4" y="40">6</text><text x="4" y="58">4</text><text x="4" y="76">2</text>
        <line x1="14" y1="92" x2="172" y2="92" stroke="#999" stroke-width="0.6"/>
        <rect x="24" y="62" width="34" height="30" fill="var(--green-pale)"/>
        <rect x="78" y="52" width="34" height="40" fill="var(--green-mid)"/>
        <rect x="132" y="34" width="34" height="58" fill="#1a4d1d"/>
        <text x="28" y="103">Y2013</text><text x="84" y="103">Y2014</text><text x="137" y="103">Y2017</text>
      </svg>

      <div class="share">
        <ul class="legend">
          <li><i style="background:#1a4d1d"></i><span>GLD</span>00%</li>
          <li><i style="background:var(--green)"></i><span>PRH</span>00%</li>
          <li><i style="background:var(--green-mid)"></i><span>NLG</span>00%</li>
          <li><i style="background:#8db27a"></i><span>LBR</span>00%</li>
          <li><i style="background:var(--green-pale)"></i><span>DHC</span>00%</li>
          <li><i style="background:#b5b5b5"></i><span>JCE</span>00%</li>
        </ul>
        <svg width="90" height="64" viewBox="0 0 90 64">
          <g transform="rotate(-90 45 32)" fill="none" stroke-width="12">
            <circle cx="45" cy="32" r="22" stroke="#1a4d1d" stroke-dasharray="30 109" stroke-dashoffset="0"/>
            <circle cx="45" cy="32" r="22" stroke="var(--green)" stroke-dasharray="26 113" stroke-dashoffset="-30"/>
            <circle cx="45" cy="32" r="22" stroke="var(--green-mid)" stroke-dasharray="24 115" stroke-dashoffset="-56"/>
            <circle cx="45" cy="32" r="22" stroke="#8db27a" stroke-dasharray="20 119" stroke-dashoffset="-80"/>
            <circle cx="45" cy="32" r="22" stroke="var(--green-pale)" stroke-dasharray="21 118" stroke-dashoffset="-100"/>
            <circle cx="45" cy="32" r="22" stroke="#b5b5b5" stroke-dasharray="18 121" stroke-dashoffset="-121"/>
          </g>
        </svg>
      </div>

      <ul class="key-points">
        <li>The Hengqin new area reportedly will not be open to gaming companies, meaning visitors wanting to gamble will still need to cross into Macau.</li>
        <li>One dark cloud may be a regulatory clampdown, with a U.S. federal commission saying there is "significant" risk of money laundering in the territory.</li>
        <li>New casino openings in Cotai between 2015 and 2018 will need between 5,000 to 8,000 new slot machines</li>
      </ul>
    </aside>

    <p class="footer">Orient Wager Digest | March 2014</p>
  </section>

</main>
</body>
</html>
```